Book cover for a very impressive real-life healing story from a stage IV deadly disease

I need a book cover design for the French translation of the US book http://www.pagevendo.com/Tims-Journey-Fever-Outlasted-Illness/dp/0845512097/ref=sr_1_4?s=books&ie=UTF8&qid=1455100794&sr=1-4&keywords=kit+marsh
.
I do not want the word AIDS on the French cover, as the story of this book applies to any disease.

The french title will be something like :
Un nouveau matin !
Condamné par la médecine, il guérit grâce au jeûne, la détoxination, et l’amour.

which means something like
A new morning!
Subtitle : Given up by official medecine, he managed to heal with fasting, detox and love.

Many thanks !

Target Market(s)

Anybody interested in natural health

Requirements
Must have
• Nothing special
Nice to have
• Nothing special
Should not have
• Nothing special

```html
<!DOCTYPE html>
<html lang="fr">
<head>
<meta charset="utf-8">
<title>Un nouveau matin ! — Kit Marsh</title>
<link rel="stylesheet" href="https://fonts.googleapis.com/css2?family=Libre+Baskerville:wght@400;700&family=Montserrat:wght@500&display=swap">
<style>
  :root {
    --wood-dark: #1d3850;
    --wood-mid: #2e5575;
    --wood-light: #3d6a8c;
    --ink: #ffffff;
    --fold: rgba(255,255,255,0.55);
  }
  * { margin: 0; padding: 0; box-sizing: border-box; }
  html, body { width: 1200px; height: 830px; overflow: hidden; background: var(--wood-dark); }
  .jacket {
    position: relative; width: 1200px; height: 830px; overflow: hidden;
    background: linear-gradient(100deg, var(--wood-dark) 0%, var(--wood-mid) 45%, var(--wood-light) 70%, var(--wood-mid) 100%);
    color: var(--ink);
    font-family: "Libre Baskerville", Georgia, serif;
  }
  .fold { position: absolute; top: 0; bottom: 0; width: 0; border-left: 1px dashed var(--fold); }
  .fold--left { left: 554px; }
  .fold--right { left: 646px; }

  .blurb {
    position: absolute; left: 63px; top: 92px; width: 424px;
    font-size: 15.2px; line-height: 23px; text-align: justify; font-weight: 700;
  }
  .blurb p { text-indent: 29px; }
  .blurb p.lead { text-indent: 0; }
  .dropcap {
    float: left; font-size: 58px; line-height: 46px; margin: 2px 4px 0 0; font-weight: 700;
  }

  .spine-title, .spine-author {
    position: absolute; left: 600px; transform-origin: left top; transform: rotate(90deg);
    white-space: nowrap; font-weight: 700; line-height: 1;
  }
  .spine-title { top: 140px; left: 625px; font-size: 29px; }
  .spine-author { top: 680px; left: 618px; font-size: 24px; }

  .herbs {
    position: absolute; left: 640px; top: 344px; width: 560px; height: 486px;
    background:
      radial-gradient(circle at 26% 22%, #8a2a24 0 16%, transparent 17%),
      radial-gradient(circle at 85% 15%, #3a4a2a 0 11%, transparent 12%),
      radial-gradient(circle at 52% 45%, #b89a70 0 13%, transparent 22%),
      radial-gradient(circle at 82% 85%, #d49a3a 0 16%, transparent 17%),
      radial-gradient(ellipse at 25% 95%, #3f8a3a 0 22%, transparent 30%),
      radial-gradient(ellipse at 55% 55%, rgba(200,175,130,0.45) 0 30%, transparent 45%);
  }

  .title {
    position: absolute; left: 672px; top: 34px; width: 508px;
    text-align: center; font-weight: 700; font-size: 78px; line-height: 104px; letter-spacing: -1px;
  }
  .subtitle {
    position: absolute; left: 672px; top: 280px; width: 508px; text-align: center;
    font-family: "Montserrat", Arial, sans-serif; font-weight: 500;
    font-size: 17px; line-height: 24px; letter-spacing: 0.8px;
  }
  .author {
    position: absolute; left: 686px; top: 702px; font-weight: 700; font-size: 45px; line-height: 1;
  }
</style>
</head>
<body>
<div class="jacket">
  <section class="back-cover">
    <div class="blurb">
      <p class="lead"><span class="dropcap">S</span>nsequia id et, culluptat quae nonsequi om molupta voloria tiorro il inctus, si occumque imusdae pedipis etur, sed minvenima ius, sitatio vel ibusae rate et mnis adis ex et dolorep ror rovidia do lores veles rerunda doleserum qui consect empedior magni voluptatium.</p>
      <p>Et omnient urenime omnis volorerci di amendae et ut aut hit, quaepellis doluptas molore latiuntoria sin nimei ncimilicid utessit, non porit eat as et inum iuscipsam inume velenec usamet viducit mintotam facesequidi cusam, corehent.</p>
      <p>Et quuntotae ex eturit aborerero id quaspit pra quodi autem hilit aut labo. Arum que eiur? Qui om nime volor simi, qui dipsum in. cilitis eaqui omnis antum illest vel iusdaes equidit et volorem et eaquis volorae re voluptam sum quibus, odio. quo bear cime eum ex earunt.</p>
      <p>Mendeni volum, odis repel ea quam voluptatum sitaeces dolupit labo. Nam alitatus.</p>
      <p>Omnihil etur amus, ut aut eiunt, inventio omnis est reruptur?</p>
      <p>Modis exerum remperrum nulpa corerep eruptat.</p>
    </div>
  </section>

  <div class="fold fold--left"></div>
  <div class="fold fold--right"></div>

  <section class="spine">
    <div class="spine-title">Un nouveau matin !</div>
    <div class="spine-author">Marsh</div>
  </section>

  <section class="front-cover">
    <div class="herbs" role="img" aria-label="Bowls of dried goji berries, herbs, calendula flowers and fresh mint on blue wooden planks"></div>
    <h1 class="title">Un nouveau<br>matin !</h1>
    <p class="subtitle">Condamné par la médecine, il guérit grâce<br>au jeûne, la détoxination, et l’amour.</p>
    <div class="author">Kit Marsh</div>
  </section>
</div>
</body>
</html>
```